Quorvane - corporate Business Card

We need a good look and innovative business card for a new start up company based in Los Angeles called "Quorvane". We are in a payment business, including payment card, app, and ewallet. We are expert in online payment and Card not present (CNP) transaction.
We need an innovative, modern business card.

Our logo font is Aero Matics

Target Market(s)

Startup - Bank - Online Payment - Card Manufacturing

Industry/Entity Type

Startup

Contact Information for Business Card

phone: 424 555 0173 - Address: 4270 Marbrook blvd, Brenwick City, CA 90417

Requirements
Must have
• Message: innovative, professional, expert, high tech, trust, online payment expert, security
Nice to have
• no comment
Should not have
• no Comment

```html
<!DOCTYPE html>
<html lang="en">
<head>
<meta charset="utf-8">
<title>Quorvane – Business Card</title>
<link rel="stylesheet" href="https://fonts.googleapis.com/css2?family=Montserrat:wght@400;700&family=Quicksand:wght@500;700&display=swap">
<style>
  :root {
    --page: #ffffff;
    --charcoal: #333333;
    --charcoal-dark: #1c1c1c;
    --charcoal-deep: #0f0f0f;
    --charcoal-mid: #2a2a2a;
    --brand-red: #b71b2f;
    --brand-red-dark: #8a1524;
    --paper: #ffffff;
  }
  html, body {
    margin: 0;
    width: 1026px;
    height: 1200px;
    overflow: hidden;
    background: var(--page);
  }
  .sheet { display: block; width: 1026px; height: 1200px; }
  .card { filter: url(#card-shadow); }
  .fill-charcoal { fill: var(--charcoal); }
  .fill-dark { fill: var(--charcoal-dark); }
  .fill-deep { fill: var(--charcoal-deep); }
  .fill-mid { fill: var(--charcoal-mid); }
  .fill-red { fill: var(--brand-red); }
  .fill-red-dark { fill: var(--brand-red-dark); }
  .fill-paper { fill: var(--paper); }
  .brand-name {
    font-family: "Quicksand", sans-serif;
    font-weight: 700;
    fill: var(--brand-red);
  }
  .person-name {
    font-family: "Montserrat", sans-serif;
    font-weight: 700;
    font-size: 40px;
    fill: var(--paper);
  }
  .person-title {
    font-family: "Montserrat", sans-serif;
    font-weight: 400;
    font-size: 23px;
    fill: var(--paper);
  }
  .contact-line {
    font-family: "Quicksand", sans-serif;
    font-weight: 500;
    font-size: 22px;
    fill: var(--paper);
  }
  .contact-phone { letter-spacing: 2px; font-size: 20px; }
  .icon-line { fill: none; stroke: var(--paper); stroke-width: 2.6; stroke-linejoin: round; stroke-linecap: round; }
  .icon-solid { fill: var(--paper); }
</style>
</head>
<body>
<svg class="sheet" viewBox="0 0 1026 1200" xmlns="http://www.w3.org/2000/svg">
  <defs>
    <filter id="card-shadow" x="-10%" y="-10%" width="120%" height="120%">
      <feDropShadow dx="0" dy="0" stdDeviation="8" flood-color="#000" flood-opacity="0.35"/>
    </filter>
  </defs>

  <!-- Card front -->
  <g class="card card-front">
    <rect class="fill-charcoal" x="95" y="83" width="854" height="512"/>
    <rect class="fill-paper" x="95" y="111" width="854" height="139"/>
    <rect class="fill-charcoal" x="95" y="250" width="91" height="196"/>
    <rect class="fill-charcoal" x="857" y="250" width="92" height="196"/>
    <polygon class="fill-dark" points="186,250 278,231 278,428 186,446"/>
    <polygon class="fill-dark" points="765,231 857,250 857,446 765,428"/>
    <rect class="fill-charcoal" x="278" y="231" width="487" height="197"/>
    <polygon class="fill-paper" points="186,446 278,428 765,428 857,446 765,468 278,468"/>
    <rect class="fill-mid" x="95" y="446" width="91" height="149"/>
    <rect class="fill-mid" x="857" y="446" width="92" height="149"/>
    <polygon class="fill-deep" points="186,446 278,468 278,595 186,595"/>
    <polygon class="fill-deep" points="765,468 857,446 857,595 765,595"/>
    <rect class="fill-charcoal" x="278" y="468" width="487" height="127"/>
    <circle class="fill-red" cx="361" cy="329" r="66"/>
    <text class="brand-name" x="442" y="352" font-size="60">Quorvane</text>
  </g>

  <!-- Card back -->
  <g class="card card-back">
    <rect class="fill-charcoal" x="95" y="633" width="859" height="515"/>
    <rect class="fill-red" x="95" y="679" width="387" height="77"/>
    <rect class="fill-paper" x="95" y="756" width="387" height="275"/>
    <rect class="fill-red" x="95" y="1031" width="387" height="78"/>
    <circle class="fill-red" cx="176" cy="902" r="53"/>
    <text class="brand-name" x="238" y="917" font-size="44">Quorvane</text>
    <g class="icon-globe" transform="translate(177 1071)">
      <circle class="icon-line" r="15"/>
      <ellipse class="icon-line" rx="6.5" ry="15"/>
      <line class="icon-line" x1="-15" y1="0" x2="15" y2="0"/>
      <line class="icon-line" x1="-13" y1="-7" x2="13" y2="-7"/>
      <line class="icon-line" x1="-13" y1="7" x2="13" y2="7"/>
    </g>
    <text class="contact-line" x="210" y="1080">web address</text>

    <rect class="fill-dark" x="482" y="633" width="68" height="515"/>
    <polygon class="fill-red-dark" points="482,679 550,668 550,746 482,756"/>
    <polygon class="fill-red-dark" points="482,795 550,803 550,881 482,873"/>
    <polygon class="fill-red-dark" points="482,916 550,927 550,1005 482,994"/>
    <polygon class="fill-red-dark" points="482,1031 550,1042 550,1119 482,1109"/>

    <rect class="fill-red" x="550" y="668" width="404" height="78"/>
    <rect class="fill-red" x="550" y="803" width="404" height="78"/>
    <rect class="fill-red" x="550" y="927" width="404" height="78"/>
    <rect class="fill-red" x="550" y="1042" width="404" height="77"/>

    <g class="icon-person" transform="translate(516 712)">
      <circle class="icon-solid" cx="0" cy="-10" r="11"/>
      <path class="icon-solid" d="M-23 22 Q-22 4 -8 2 L0 8 L8 2 Q22 4 23 22 Z"/>
      <path class="icon-line" d="M-14 -10 A14 14 0 0 1 14 -10"/>
    </g>
    <g class="icon-phone" transform="translate(516 837)">
      <path class="icon-solid" d="M-18 -6 Q-18 -16 0 -16 Q18 -16 18 -6 L12 -2 L8 -8 L-8 -8 L-12 -2 Z"/>
      <path class="icon-solid" d="M-9 -4 L9 -4 L15 14 L-15 14 Z"/>
      <circle cx="0" cy="5" r="5" fill="var(--brand-red-dark)"/>
    </g>
    <g class="icon-mail" transform="translate(516 962)">
      <rect class="icon-line" x="-17" y="-11" width="34" height="22" rx="2"/>
      <polyline class="icon-line" points="-17,-10 0,3 17,-10"/>
    </g>
    <g class="icon-home" transform="translate(517 1078)">
      <path class="icon-line" d="M-16 -1 L0 -15 L16 -1 M-12 -4 L-12 15 L-4 15 L-4 4 L4 4 L4 15 L12 15 L12 -4"/>
    </g>

    <text class="person-name" x="589" y="708">NAME</text>
    <text class="person-title" x="589" y="733">Postion/ Title</text>
    <text class="contact-line contact-phone" x="576" y="848">424 555 0173</text>
    <text class="contact-line" x="583" y="969">Email</text>
    <text class="contact-line" x="576" y="1075">4270 Marbrook blvd,</text>
    <text class="contact-line" x="576" y="1102">Brenwick City, CA 90417</text>
  </g>
</svg>
</body>
</html>
```